Company Profile for Consulting Comany

Need Company profile to be designed in a professional way.

for inspiring :-
https://www.folivane.net/gallery/5372904/COMPANY-PROFILE
https://www.folivane.net/gallery/60391742/Biotech-Product-Catalog-No1-(Laminar-Air-Flow)
https://www.folivane.net/gallery/73905218/MPG-Globalpath-Company-Profile-2014-(MPG-Rebrand-part-2)

Target Market(s)

Corporate

Industry/Entity Type

It Company

Font styles to use
Sans Serif

Requirements
Must have
• Landscape A4 size
• Must go with the logo branding
• Must Have Visual Identity is the most important
• Must Have mpty spaces

```html
<!DOCTYPE html>
<html lang="en">
<head>
<meta charset="utf-8">
<title>Our Team – Company Profile Spread</title>
<link rel="stylesheet" href="https://fonts.googleapis.com/css2?family=Lato:wght@400;700;900&family=Open+Sans:wght@400;600;700&display=swap">
<style>
  :root {
    --backdrop: #5b5b5d;
    --paper: #ffffff;
    --ink-dark: #111111;
    --page-black: #000000;
    --spine-grey: #262626;
    --text-light: #ffffff;
    --photo-tone: #8a8a8a;
    --photo-empty: #666666;
    --folio-line: #9a9a9a;
  }
  * { margin: 0; padding: 0; box-sizing: border-box; }
  html, body { width: 1200px; height: 591px; overflow: hidden; }
  body { background: var(--backdrop); position: relative; font-family: "Open Sans", sans-serif; }

  .spread { position: absolute; left: 100px; top: 119px; width: 1000px; height: 352px; }
  .cover-panel { position: absolute; top: 0; width: 188px; height: 352px; background: var(--paper); }
  .cover-panel--left { left: 0; }
  .cover-panel--right { left: 812px; }
  .section-title {
    position: absolute; top: 155px; width: 100%; text-align: center;
    font-family: "Lato", sans-serif; font-weight: 900; font-size: 20px; line-height: 21px;
    color: var(--ink-dark); letter-spacing: 0.3px;
  }
  .section-title--left { left: 32px; width: 66px; }
  .section-title--right { left: 70px; width: 66px; }

  .page { position: absolute; top: 0; width: 312px; height: 352px; }
  .page--left { left: 188px; background: linear-gradient(90deg, var(--page-black) 0%, var(--page-black) 62%, var(--spine-grey) 100%); }
  .page--right { left: 500px; background: linear-gradient(90deg, var(--spine-grey) 0%, var(--page-black) 30%, var(--page-black) 100%); }

  .member { position: absolute; color: var(--text-light); }
  .member__photo { width: 44px; height: 44px; background: linear-gradient(160deg, #a5a5a5, #5e5e5e); }
  .member__photo--empty { background: var(--photo-empty); }
  .member__head { position: relative; height: 49px; }
  .member__id { position: absolute; left: 48px; bottom: 5px; white-space: nowrap; }
  .member__name { font-family: "Open Sans", sans-serif; font-weight: 700; font-size: 6.3px; line-height: 8px; text-transform: uppercase; }
  .member__role { font-size: 4.6px; line-height: 6px; text-transform: uppercase; }
  .member__bio { font-size: 4.7px; line-height: 7.2px; }

  .folio {
    position: absolute; top: 337px; width: 8px; height: 8px; border: 0.7px solid var(--folio-line);
    border-radius: 50%; color: var(--folio-line); font-size: 4.5px; line-height: 6.6px; text-align: center;
  }
</style>
</head>
<body>
  <main class="spread">
    <section class="cover-panel cover-panel--left">
      <h1 class="section-title section-title--left">OUR TEAM</h1>
    </section>

    <section class="page page--left">
      <article class="member" style="left:37px; top:183px; width:118px;">
        <div class="member__head">
          <div class="member__photo" role="img" aria-label="Portrait photo of Tariq Al Mansouri"></div>
          <div class="member__id">
            <div class="member__name">Tariq Al Mansouri</div>
            <div class="member__role">Consulting Manager</div>
          </div>
        </div>
        <p class="member__bio">Certified HR Practitioner with more than 15 years of exceptional local and international business track record in talent &amp; OD; combines worked in several industries including textile, F&amp;B, Construction, Retail (Marketon), Pharmaceutical, Education and Chemicals Manufacturing (Purelab-Norco). Diversified educational achievement starting from computer programming, Business Administration, IPHD diploma in HR Practices and other relative certifications.</p>
      </article>

      <article class="member" style="left:164px; top:97px; width:124px;">
        <div class="member__head">
          <div class="member__photo" role="img" aria-label="Portrait photo of Khalid Haddad"></div>
          <div class="member__id">
            <div class="member__name">Khalid Haddad</div>
            <div class="member__role">Senior Consultant</div>
          </div>
        </div>
        <p class="member__bio">Certified HR Practitioner with more than 12 years of experience working in Gulfstar Energy and Nadira Chemical Company as well as in the private sector as an independent consultant. Khalid holds a B.S. in Chemical Engineering and holds certifications in Coaching, Change Management, O.D, and Leadership Assessment &amp; Development. Khalid's areas of strength are engaging teams in profound change interventions either through coaching or facilitative learning in workshops specifically in Leadership development and personal mastery.</p>
      </article>

      <div class="folio" style="left:157px;">7</div>
    </section>

    <section class="page page--right">
      <article class="member" style="left:38px; top:97px; width:124px;">
        <div class="member__head">
          <div class="member__photo" role="img" aria-label="Portrait photo of Faisal Al-Qahtan"></div>
          <div class="member__id">
            <div class="member__name">Faisal Al-Qahtan</div>
            <div class="member__role">Projects Manager</div>
          </div>
        </div>
        <p class="member__bio">Certified NEXA Portfolio Manager and an IT Professional with more than ten years of experience and in-depth understanding of NEXA Project Implementations, mainly leading HR, Training, Recruitment and other affiliates projects. Faisal has performed implementations of NEXA Business Packages for EP namely; ESS/MSS, NEXA BO BI, NEXA BO upgrade to BI 4.0, NEXA BO Access Control, NEXA Enterprise Learning Solutions, NEXA LVC, Panavera implementation with NEXA integration, Medium implementation and intranet on TeamPortal. Faisal has also participated in the NEXA rollout to 13 affiliate companies in TANWIR all around the Kingdom.</p>
      </article>

      <article class="member" style="left:164px; top:183px; width:118px;">
        <div class="member__head">
          <div class="member__photo member__photo--empty" role="img" aria-label="Portrait photo of Samir Lahlouyan"></div>
          <div class="member__id">
            <div class="member__name">Samir Lahlouyan</div>
            <div class="member__role">Consultant</div>
          </div>
        </div>
        <p class="member__bio">This is dummy copy. Required original copy about Samir Lahlouyan. This is dummy copy. Required original copy about Samir Lahlouyan. This is dummy copy. Required original copy about Samir Lahlouyan. This is dummy copy. Required original copy about Samir Lahlouyan. This is dummy copy. Required original copy about Samir Lahlouyan. This is dummy copy. Required original copy about Samir Lahlouyan. This is dummy copy. Required original copy about Samir Lahlouyan. This is dummy copy. Required original copy about Samir Lahlouyan.</p>
      </article>

      <div class="folio" style="left:246px;">8</div>
    </section>

    <section class="cover-panel cover-panel--right">
      <h2 class="section-title section-title--right">OUR TEAM</h2>
    </section>
  </main>
</body>
</html>
```